Estate Planner needs an Ad for a local newsletter

I need an ad designed for my practice as an estate planning attorney. The ad will be in a newsletter that targets individuals over the age of 55. My ad is 7.5"W x 4.6"H (a half page ad) .
The wording should include:
Varnholt, Danielle

Danielle Varnholt

Wisdom Meets Planning
Your Estate, Your Legacy

After 23 years as a military spouse, moving our family of six across the country,
I learned the true value of careful planning. Today I help Palomar County's seniors protect what matters most – their family’s future and their life’s work.

I understand that your estate is more than just assets – it's a lifetime of wise
decisions, cherished memories, and dreams for your family's future.

Professional Estate Planning:
• Wills & Living Trusts • Healthcare Directives
• Power of Attorney • Asset Protection
• Probate Avoidance • Peace of Mind

Plus also needs to have my contact information:
RPV Law
Danielle Varnholt
Attorney/Of Counsel
4712 Cedarbrook Lane
Halvern, Florida 39012
(555) 684-1093
dvarnholt@rpvlegalteam.example
Logo is attached.

```html
<!DOCTYPE html>
<html lang="en">
<head>
<meta charset="utf-8">
<title>RPV Law – Estate Planning Ad</title>
<link rel="stylesheet" href="https://fonts.googleapis.com/css2?family=Bebas+Neue&family=Barlow+Condensed:wght@300;400;500;600&family=Open+Sans:wght@700&family=Rubik:wght@600&display=swap">
<style>
  :root {
    --page: #ffffff;
    --navy: #13233f;
    --band-blue: #064c8a;
    --accent-blue: #3a8fd6;
    --white: #ffffff;
    --ink: #0f1d38;
    --photo-dark: #6f6a62;
    --photo-warm: #c8b49a;
    --photo-light: #e8edf4;
  }
  * { box-sizing: border-box; margin: 0; padding: 0; }
  html, body { width: 1200px; height: 1200px; overflow: hidden; background: var(--page); }
  .ad {
    position: absolute; left: 109px; top: 301px; width: 989px; height: 605px;
    overflow: hidden; box-shadow: 5px 6px 6px rgba(0,0,0,.45);
    font-family: "Barlow Condensed", sans-serif; color: var(--white);
  }
  .ad > * { position: absolute; }
  .photo {
    inset: 0 0 106px 0;
    background:
      radial-gradient(ellipse 40% 45% at 85% 35%, rgba(222,170,110,.75), transparent 70%),
      radial-gradient(ellipse 35% 30% at 50% 10%, rgba(245,245,240,.9), transparent 70%),
      linear-gradient(180deg, var(--photo-dark) 0%, var(--photo-warm) 35%, #d9d6d0 55%, var(--photo-light) 75%, #dbe3ee 100%);
  }
  .shapes { inset: 0; width: 989px; height: 605px; }
  .footer { left: 0; top: 499px; width: 989px; height: 106px; background: var(--navy); }
  .brand { left: 23px; top: 33px; width: 166px; }
  .brand-name { display: flex; align-items: center; gap: 8px; font-size: 34px; font-weight: 600; line-height: 1; }
  .brand-mark { width: 14px; height: 14px; background: var(--white); }
  .brand-partners { margin-top: 5px; font-size: 7.5px; font-weight: 600; letter-spacing: .2px; white-space: nowrap; }
  .headline { left: 23px; top: 146px; font-family: "Bebas Neue", sans-serif; font-weight: 400; font-size: 37px; line-height: 44px; letter-spacing: 0; }
  .headline .lead { color: var(--accent-blue); display: block; }
  .headline .rest { color: var(--white); display: block; }
  .contact-icon { left: 23px; top: 410px; width: 74px; height: 72px; }
  .details-label { left: 127px; top: 408px; font-size: 29px; font-weight: 300; line-height: 1; }
  .details-phone { left: 123px; top: 440px; font-family: "Open Sans", sans-serif; font-weight: 700; font-size: 33px; line-height: 1; }
  .services-title { left: 546px; top: 340px; font-family: "Rubik", sans-serif; font-weight: 600; font-size: 27px; color: #0b0b0b; line-height: 1.2; }
  .services { list-style: none; left: 548px; top: 390px; width: 440px; display: grid; grid-template-columns: 241px 199px; row-gap: 5px; color: var(--ink); font-size: 21px; font-weight: 500; line-height: 26px; }
  .services li { display: flex; align-items: center; gap: 12px; }
  .services li:nth-child(5), .services li:nth-child(6) { margin-top: 4px; }
  .services svg { width: 24px; height: 12px; flex: none; }
  .pin-icon { left: 105px; top: 519px; width: 68px; height: 68px; }
  .address { left: 194px; top: 513px; font-size: 18.5px; font-weight: 500; line-height: 24px; font-style: normal; }
  .divider { left: 542px; top: 515px; width: 2px; height: 77px; background: var(--white); }
  .mail-icon { left: 586px; top: 521px; width: 52px; height: 64px; }
  .email { left: 656px; top: 541px; font-size: 18.5px; font-weight: 500; }
</style>
</head>
<body>
<div class="ad">
  <div class="photo" role="img" aria-label="Photo of a hand signing estate documents beside a small wooden model house on a desk"></div>

  <svg class="shapes" viewBox="0 0 989 605" aria-hidden="true">
    <defs>
      <linearGradient id="accentGrad" x1="0" y1="0" x2="1" y2="1">
        <stop offset="0" stop-color="#0a3566"/><stop offset="1" stop-color="#2b74c2"/>
      </linearGradient>
    </defs>
    <polygon points="0,0 367,0 541,302 505,393 0,393" fill="var(--navy)"/>
    <polygon points="505,366 528,393 490,393" fill="url(#accentGrad)"/>
    <polygon points="0,393 528,393 469,499 0,499" fill="var(--band-blue)"/>
  </svg>

  <div class="footer"></div>

  <div class="brand">
    <div class="brand-name">RPV Law <span class="brand-mark"></span></div>
    <div class="brand-partners">de Ravelle · Pinter · Voss · Marlowe · Quill</div>
  </div>

  <h1 class="headline">
    <span class="lead">I understand that your estate is<br>more than just assets</span>
    <span class="rest">It's a lifetime of wise decisions,<br>cherished memories,&nbsp; and dreams for<br>your family's future.</span>
  </h1>

  <svg class="contact-icon" viewBox="0 0 74 72" fill="none" stroke="#fff" stroke-width="2.4" stroke-linecap="round" aria-hidden="true">
    <rect x="8" y="2" width="58" height="68" rx="5"/>
    <path d="M66 12h5v48h-5"/>
    <path d="M2 14h11M2 28h11M2 42h11M2 56h11"/>
    <circle cx="37" cy="24" r="6"/>
    <path d="M26 40c0-7 5-10 11-10s11 3 11 10z"/>
    <path d="M27 49h20M27 55h20M31 61h12"/>
  </svg>
  <div class="details-label">For More Details</div>
  <div class="details-phone">(555) 684-1093</div>

  <h2 class="services-title">Professional Estate Planning:</h2>
  <ul class="services">
    <li><svg viewBox="0 0 24 12" fill="none" stroke="#0f1d38" stroke-width="1.4"><path d="M1 6h16M13 2l5 4-5 4M1 3v6"/></svg>Wills &amp; Living Trusts</li>
    <li><svg viewBox="0 0 24 12" fill="none" stroke="#0f1d38" stroke-width="1.4"><path d="M1 6h16M13 2l5 4-5 4M1 3v6"/></svg>Asset Protection</li>
    <li><svg viewBox="0 0 24 12" fill="none" stroke="#0f1d38" stroke-width="1.4"><path d="M1 6h16M13 2l5 4-5 4M1 3v6"/></svg>Healthcare Directives</li>
    <li><svg viewBox="0 0 24 12" fill="none" stroke="#0f1d38" stroke-width="1.4"><path d="M1 6h16M13 2l5 4-5 4M1 3v6"/></svg>Probate Avoidance</li>
    <li><svg viewBox="0 0 24 12" fill="none" stroke="#0f1d38" stroke-width="1.4"><path d="M1 6h16M13 2l5 4-5 4M1 3v6"/></svg>Power of Attorney</li>
    <li><svg viewBox="0 0 24 12" fill="none" stroke="#0f1d38" stroke-width="1.4"><path d="M1 6h16M13 2l5 4-5 4M1 3v6"/></svg>Peace of Mind</li>
  </ul>

  <svg class="pin-icon" viewBox="0 0 68 68" fill="none" stroke="#fff" stroke-width="1.8" aria-hidden="true">
    <path d="M34 56 20 36a17 17 0 1 1 28 0z"/>
    <circle cx="34" cy="24" r="9"/>
    <ellipse cx="34" cy="60" rx="22" ry="5"/>
    <circle cx="6" cy="6" r="3"/><circle cx="62" cy="7" r="3"/><circle cx="6" cy="44" r="3"/><circle cx="60" cy="42" r="4"/>
    <path d="M0 67h68"/>
  </svg>
  <address class="address">RPV Law , Danielle Varnholt<br>Attorney/ Of Counsel, 4712 Cedarbrook Lane,<br>Halvern, Florida 39012</address>

  <div class="divider"></div>

  <svg class="mail-icon" viewBox="0 0 52 64" fill="none" stroke="#fff" stroke-width="1.8" stroke-linejoin="round" aria-hidden="true">
    <path d="M9 26V2h34v24"/>
    <path d="M2 22l7-6M50 22l-7-6"/>
    <rect x="2" y="22" width="48" height="40" rx="3"/>
    <path d="M2 24l24 20 24-20M2 62l18-15M50 62 32 47"/>
    <circle cx="26" cy="16" r="6"/><path d="M32 16v3a3 3 0 0 0 5-2 11 11 0 1 0-5 9"/>
    <path d="M20 53h12M23 57h6"/>
  </svg>
  <div class="email">dvarnholt@rpvlegalteam.example</div>
</div>
</body>
</html>
```